3D Brochure
Brochure
Project: 3D Brochure
3D Brochure - Environment
Creative Brief
Environment
Corporate, Industrial
Trifold brochure. Must include some "Bleed" for printing.

```html
<!DOCTYPE html>
<html lang="en">
<head>
<meta charset="utf-8">
<title>Northline Environmental – Trifold Brochure</title>
<link href="https://fonts.googleapis.com/css2?family=Open+Sans:wght@400;600;700&family=Roboto+Condensed:wght@700&display=swap" rel="stylesheet">
<style>
:root{
  --bg:#dcdcdc;
  --dark:#1c2126;
  --dark-2:#262c33;
  --dark-3:#323a43;
  --light:#eef0f2;
  --blue:#1f8fd2;
  --blue-light:#48b6ea;
  --text-light:#d7dde3;
  --text-dark:#3a4148;
  --photo-a:#7d8a96;
  --photo-b:#b9c3cc;
}
*{margin:0;padding:0;box-sizing:border-box}
html,body{width:1200px;height:478px;overflow:hidden;background:var(--bg)}
body{position:relative;font-family:"Open Sans",Arial,sans-serif}
.brochure{position:absolute;box-shadow:0 3px 10px rgba(0,0,0,.35);overflow:hidden}
.outside{left:44px;top:26px;width:536px;height:426px;display:flex}
.inside{left:612px;top:20px;width:548px;height:438px;background:var(--dark)}
.panel{position:relative;width:33.333%;height:100%;overflow:hidden}
.panel-back{background:var(--light);padding:22px 14px;color:var(--text-dark)}
.panel-contact{background:var(--dark-2);color:var(--text-light);padding:22px 14px}
.panel-cover{background:var(--dark)}
.heading-light{font-family:"Roboto Condensed",Arial,sans-serif;font-size:10px;color:var(--blue);letter-spacing:.4px;text-transform:uppercase;margin-bottom:6px}
.body-small{font-size:6.5px;line-height:1.5}
.bullets{list-style:none;font-size:6.5px;line-height:1.7}
.bullets li::before{content:"";display:inline-block;width:4px;height:4px;background:var(--blue);margin-right:5px;vertical-align:middle}
.rule{height:1px;background:var(--blue);margin:14px 0 12px}
.photo{background:linear-gradient(135deg,var(--photo-a),var(--photo-b));border-radius:2px}
.back-photo{position:absolute;left:14px;right:14px;bottom:22px;height:170px}
.contact-title{font-family:"Roboto Condensed",Arial,sans-serif;font-size:11px;text-align:center;color:#fff;margin:142px 0 12px;letter-spacing:.5px}
.contact-list{display:grid;grid-template-columns:1fr auto;gap:5px 8px;font-size:7px;padding:0 8px}
.office-title{font-family:"Roboto Condensed",Arial,sans-serif;font-size:10px;text-align:center;margin:30px 0 6px;color:#fff}
.office{font-size:6.5px;text-align:center;line-height:1.6}
.response{position:absolute;left:0;right:0;bottom:0;height:46px;background:var(--blue);color:#fff;text-align:center;font-family:"Roboto Condensed",Arial,sans-serif;padding-top:9px}
.response strong{display:block;font-size:11px}
.response span{font-size:12px}
.cover-brand{position:absolute;top:30px;left:0;right:0;text-align:center}
.brand-dot{width:26px;height:26px;border-radius:50%;background:var(--blue);margin:0 auto 8px}
.brand-name{font-size:10px;font-weight:600;color:#fff}
.cover-photo-1{position:absolute;left:10px;right:10px;top:130px;height:120px}
.cover-photo-2{position:absolute;left:10px;right:10px;top:258px;height:110px}
.cover-band{position:absolute;left:0;right:0;bottom:0;height:46px;background:linear-gradient(180deg,var(--dark),var(--blue))}

.inside-header{height:40px;display:flex;justify-content:space-between;align-items:center;padding:0 16px;border-bottom:2px solid var(--blue)}
.inside-brand{display:flex;align-items:center;gap:8px;font-size:12px;font-weight:600;color:#fff}
.inside-brand i{width:16px;height:16px;border-radius:50%;background:var(--blue);display:block}
.inside-phone{font-family:"Roboto Condensed",Arial,sans-serif;font-size:18px;color:#fff}
.columns{display:flex;gap:10px;padding:10px}
.column{flex:1;display:flex;flex-direction:column;gap:8px}
.service{background:var(--dark-2);padding:7px;color:var(--text-light)}
.service-title{font-family:"Roboto Condensed",Arial,sans-serif;font-size:9.5px;color:#fff;background:linear-gradient(90deg,var(--blue),var(--dark-3));padding:3px 6px;margin:-7px -7px 6px}
.service .photo{height:58px;margin-bottom:5px}
.row{display:flex;gap:6px}
.row .photo{flex:0 0 68px;height:52px;margin:0}
</style>
</head>
<body>

<section class="brochure outside">
  <div class="panel panel-back">
    <h2 class="heading-light">Credential &amp; Qualification</h2>
    <p class="body-small">Our team holds current state hazardous waste permits and federal transport certifications for every job.</p>
    <div class="rule"></div>
    <h2 class="heading-light">Credential &amp; Qualification</h2>
    <ul class="bullets">
      <li>OSHA HAZWOPER</li><li>DOT Certified</li><li>EPA Registered</li>
      <li>Confined Space Entry</li><li>Spill Response Trained</li>
      <li>Fully Insured Fleet</li><li>State Licensed Hauler</li>
    </ul>
    <div class="photo back-photo" role="img" aria-label="Tanker truck on a job site"></div>
  </div>

  <div class="panel panel-contact">
    <div class="photo" role="img" aria-label="Vacuum tanker truck on site" style="position:absolute;left:0;right:0;top:0;height:120px"></div>
    <h2 class="contact-title">EMERGENCY CONTACT</h2>
    <div class="contact-list">
      <span>Dana Morrow</span><span>555-010-3381</span>
      <span>Evan Pryce</span><span>555-010-4472</span>
      <span>Lena Ortiz</span><span>555-010-5563</span>
    </div>
    <h3 class="office-title">OFFICE</h3>
    <p class="office">120 Harbor Road, Suite 4<br>Bayview, MD 21000<br>info@northlineenv.com</p>
    <div class="response"><strong>24 HOUR RESPONSE</strong><span>555-014-2290</span></div>
  </div>

  <div class="panel panel-cover">
    <div class="cover-brand">
      <div class="brand-dot"></div>
      <div class="brand-name">Northline Environmental, LLC</div>
    </div>
    <div class="photo cover-photo-1" role="img" aria-label="Tanker truck parked at industrial yard"></div>
    <div class="photo cover-photo-2" role="img" aria-label="Crew member cleaning equipment"></div>
    <div class="cover-band" role="img" aria-label="Decorative blue wave band"></div>
  </div>
</section>

<section class="brochure inside">
  <header class="inside-header">
    <div class="inside-brand"><i></i>Northline Environmental, LLC</div>
    <div class="inside-phone">555-014-2290</div>
  </header>
  <div class="columns">
    <div class="column">
      <article class="service">
        <h3 class="service-title">Accident / Spill Cleanup</h3>
        <div class="photo" role="img" aria-label="Spill cleanup crew at roadside"></div>
        <p class="body-small">Rapid containment and recovery of hazardous liquids at road, rail and industrial sites.</p>
        <ul class="bullets"><li>Fuel spills</li><li>Chemical releases</li><li>Soil remediation</li><li>Site restoration</li></ul>
      </article>
      <div class="photo" role="img" aria-label="Bulk tanker trailer" style="height:112px"></div>
    </div>
    <div class="column">
      <article class="service">
        <h3 class="service-title">Vacuum Truck Services</h3>
        <div class="row"><div class="photo" role="img" aria-label="Vacuum truck"></div><p class="body-small">Liquid and solid removal for pits, sumps, drains and lagoons.</p></div>
      </article>
      <article class="service">
        <h3 class="service-title">Tank Cleaning</h3>
        <div class="row"><div class="photo" role="img" aria-label="Worker cleaning a tank"></div><p class="body-small">Full cleaning of above and below ground tanks, including sludge removal and disposal.</p></div>
      </article>
      <article class="service">
        <h3 class="service-title">Bulk Transformation</h3>
        <p class="body-small">Transport of bulk liquids and waste to licensed treatment facilities.</p>
        <ul class="bullets"><li>Tanker hauling</li><li>Waste manifesting</li></ul>
      </article>
    </div>
    <div class="column">
      <article class="service">
        <h3 class="service-title">Marine Service / Harbor Boom</h3>
        <div class="photo" role="img" aria-label="Harbor boom deployed on water"></div>
        <p class="body-small">Harbor boom deployment and skimming to protect waterways from oil and fuel.</p>
        <ul class="bullets"><li>Boom deployment</li><li>Oil skimming</li><li>Shoreline cleanup</li></ul>
      </article>
      <article class="service">
        <h3 class="service-title">Liquid Storage</h3>
        <div class="photo" role="img" aria-label="Row of storage tanks"></div>
        <p class="body-small">Secure temporary storage tanks available for short or long term projects.</p>
        <ul class="bullets"><li>Frac tanks</li><li>Poly tanks</li><li>Containment berms</li></ul>
      </article>
    </div>
  </div>
</section>

</body>
</html>
```